physical therapy flyer

2 office locations speciality programs - work injury / Motor vehicle accidents - spanish speaking - do not put balance defecits/ fall prevention - Spanish speaking
neck and back pain shoulder pain/ rotator cuff disorder / bursitis
hip pain knee andle and foot pain post operative care including Spine , shoulder , knee , total joint replacement

Meadowline Physical therapy & Chiropractic
4827 Larchmont BLvd
kelso park ny 11592
7185521847
3719 Bexley Parkway
Bronx NY 11592
7189024613
www.meadowlineptclinic.com

```html
<!DOCTYPE html>
<html lang="en">
<head>
<meta charset="utf-8">
<title>Meadowline Physical Therapy Flyer</title>
<link href="https://fonts.googleapis.com/css2?family=Roboto:wght@400;500;700&family=Roboto+Condensed:wght@600&display=swap" rel="stylesheet">
<style>
:root{
  --page:#ffffff;
  --green-top-a:#4f9a24;
  --green-top-b:#7cc23c;
  --dark-a:#1d3a17;
  --dark-b:#0f2410;
  --lime:#a5d33c;
  --tick:#8cc63f;
  --white:#ffffff;
  --band-gray:#dddddd;
  --heading:#333333;
  --loc-dark:#21874b;
  --loc-lime:#9ad134;
  --loc-ink:#3a3a3a;
  --footer:#3e3e3e;
}
*{margin:0;padding:0;box-sizing:border-box}
html,body{width:927px;height:1200px;overflow:hidden;background:var(--page)}
body{font-family:"Roboto",Arial,sans-serif;position:relative}
.flyer{position:absolute;left:60px;top:60px;width:800px;height:1070px}
.hero{position:absolute;left:0;top:0;width:800px;height:278px;
  background:linear-gradient(100deg,var(--green-top-a),var(--green-top-b) 55%,var(--green-top-a));}
.brand{position:absolute;left:158px;top:34px;display:flex;align-items:flex-end;gap:18px}
.brand-mark{width:74px;height:74px;border-radius:50%;background:var(--white);opacity:.92;margin-bottom:10px}
.brand-name{color:var(--white);font-size:32px;font-weight:400;line-height:34px}
.programs{position:absolute;left:0;width:800px;top:186px;text-align:center;color:var(--white);font-size:23px;line-height:29px}
.conditions{position:absolute;left:0;top:278px;width:800px;height:243px;
  background:linear-gradient(90deg,var(--dark-a),var(--dark-b) 50%,var(--dark-a));}
.condition-list{position:absolute;top:20px;list-style:none;color:var(--white);font-size:26px;line-height:39px}
.condition-list.left{left:64px}
.condition-list.right{left:425px}
.condition-list li{display:flex;align-items:center;gap:19px}
.condition-list svg{width:22px;height:22px;flex:none}
.postop{position:absolute;left:0;width:800px;text-align:center;font-size:26px}
.postop.lead{top:146px;color:var(--lime)}
.postop.areas{top:184px;color:var(--white)}
.imagery{position:absolute;left:0;top:521px;width:800px;height:271px;display:flex}
.imagery .back{width:400px;height:100%;background:radial-gradient(ellipse at 52% 50%,#d8804e 0,#8a8c92 30%,#5f6168 70%,#3e4046)}
.imagery .knee{width:400px;height:100%;background:radial-gradient(ellipse at 52% 40%,#f4c35a 0,#e86a3a 14%,#3f8ccc 40%,#1d5ea0 80%)}
.locations-title{position:absolute;left:0;top:792px;width:800px;height:64px;background:var(--band-gray);
  font-family:"Roboto Condensed",Arial,sans-serif;font-weight:600;font-size:33px;color:var(--heading);
  text-align:center;line-height:64px}
.office{position:absolute;top:856px;width:400px;height:154px}
.office.one{left:0;background:var(--loc-dark);color:var(--white)}
.office.two{left:400px;background:var(--loc-lime);color:var(--loc-ink)}
.office .icon{position:absolute;left:55px;width:30px;height:30px}
.office .icon.pin{top:20px}
.office .icon.phone{top:102px}
.office .address{position:absolute;left:105px;top:16px;font-size:21px;line-height:26px;letter-spacing:.3px}
.office .phone-number{position:absolute;left:104px;top:94px;font-size:38px;font-weight:700;letter-spacing:.3px}
.site{position:absolute;left:0;top:1010px;width:800px;height:60px;background:var(--footer);
  display:flex;align-items:center;justify-content:center;gap:14px;color:var(--white);font-size:24px}
.site svg{width:28px;height:28px}
</style>
</head>
<body>
<main class="flyer">
  <header class="hero" role="img" aria-label="Therapist treating a patient's shoulder, tinted green">
    <div class="brand">
      <span class="brand-mark"></span>
      <span class="brand-name">Meadowline Physical Therapy,<br>Chiropractic, and Acupuncture</span>
    </div>
    <p class="programs">Work injury / Motor vehicle accidents - Spanish speaking<br>Do not put balance defecits/ fall prevention - Spanish speaking</p>
  </header>

  <section class="conditions">
    <ul class="condition-list left">
      <li><svg viewBox="0 0 22 22"><circle cx="11" cy="11" r="10" fill="var(--tick)"/><path d="M6 11.5l3.5 3.5L16 8" fill="none" stroke="var(--dark-a)" stroke-width="2.6"/></svg>Neck &amp; back pain</li>
      <li><svg viewBox="0 0 22 22"><circle cx="11" cy="11" r="10" fill="var(--tick)"/><path d="M6 11.5l3.5 3.5L16 8" fill="none" stroke="var(--dark-a)" stroke-width="2.6"/></svg>Rotator cuff disorder</li>
      <li><svg viewBox="0 0 22 22"><circle cx="11" cy="11" r="10" fill="var(--tick)"/><path d="M6 11.5l3.5 3.5L16 8" fill="none" stroke="var(--dark-a)" stroke-width="2.6"/></svg>Hip pain</li>
    </ul>
    <ul class="condition-list right">
      <li><svg viewBox="0 0 22 22"><circle cx="11" cy="11" r="10" fill="var(--tick)"/><path d="M6 11.5l3.5 3.5L16 8" fill="none" stroke="var(--dark-a)" stroke-width="2.6"/></svg>Shoulder pain</li>
      <li><svg viewBox="0 0 22 22"><circle cx="11" cy="11" r="10" fill="var(--tick)"/><path d="M6 11.5l3.5 3.5L16 8" fill="none" stroke="var(--dark-a)" stroke-width="2.6"/></svg>Bursitis</li>
      <li><svg viewBox="0 0 22 22"><circle cx="11" cy="11" r="10" fill="var(--tick)"/><path d="M6 11.5l3.5 3.5L16 8" fill="none" stroke="var(--dark-a)" stroke-width="2.6"/></svg>Knee andle &amp; foot pain</li>
    </ul>
    <p class="postop lead">Post operative care including</p>
    <p class="postop areas">Spine, Shoulder, Knee , Total joint replacement</p>
  </section>

  <section class="imagery">
    <div class="back" role="img" aria-label="Person holding lower back with highlighted spine"></div>
    <div class="knee" role="img" aria-label="Hands on a knee with glowing joint highlight on blue x-ray view"></div>
  </section>

  <h2 class="locations-title">2 OFFICE LOCATIONS</h2>

  <section class="office one">
    <svg class="icon pin" viewBox="0 0 30 30"><circle cx="15" cy="15" r="14" fill="#fff" stroke="#111" stroke-width="2"/><path d="M15 7a5.5 5.5 0 0 0-5.5 5.5c0 4 5.5 10 5.5 10s5.5-6 5.5-10A5.5 5.5 0 0 0 15 7z" fill="#111"/><circle cx="15" cy="12.5" r="2" fill="#fff"/></svg>
    <p class="address">4827 Larchmont BLvd<br>Kelso park NY 11592</p>
    <svg class="icon phone" viewBox="0 0 30 30"><circle cx="15" cy="15" r="14" fill="#fff" stroke="#111" stroke-width="2"/><path d="M10.5 8.5l2.5-.5 1.5 3.5-1.6 1.2a8 8 0 0 0 4.4 4.4l1.2-1.6 3.5 1.5-.5 2.5c-.3.8-1.2 1.2-2 1-5-1.2-9-5.2-10.2-10.2-.2-.8.2-1.6 1.2-1.8z" fill="#111"/></svg>
    <p class="phone-number">7185521847</p>
  </section>

  <section class="office two">
    <svg class="icon pin" viewBox="0 0 30 30"><circle cx="15" cy="15" r="14" fill="#fff" stroke="#111" stroke-width="2"/><path d="M15 7a5.5 5.5 0 0 0-5.5 5.5c0 4 5.5 10 5.5 10s5.5-6 5.5-10A5.5 5.5 0 0 0 15 7z" fill="#111"/><circle cx="15" cy="12.5" r="2" fill="#fff"/></svg>
    <p class="address">3719 Bexley Parkway<br>Bronx NY 11592</p>
    <svg class="icon phone" viewBox="0 0 30 30"><circle cx="15" cy="15" r="14" fill="#fff" stroke="#111" stroke-width="2"/><path d="M10.5 8.5l2.5-.5 1.5 3.5-1.6 1.2a8 8 0 0 0 4.4 4.4l1.2-1.6 3.5 1.5-.5 2.5c-.3.8-1.2 1.2-2 1-5-1.2-9-5.2-10.2-10.2-.2-.8.2-1.6 1.2-1.8z" fill="#111"/></svg>
    <p class="phone-number">7189024613</p>
  </section>

  <footer class="site">
    <svg viewBox="0 0 28 28"><circle cx="14" cy="14" r="13" fill="#fff"/><g fill="none" stroke="#222" stroke-width="1.5"><circle cx="14" cy="14" r="8"/><ellipse cx="14" cy="14" rx="3.5" ry="8"/><path d="M6 14h16M7.5 10h13M7.5 18h13"/></g></svg>
    <span>www.meadowlineptclinic.com</span>
  </footer>
</main>
</body>
</html>
```